Tamsel wine Label, 750ml bottle

We need a wine label that is simple, clean, and timeless. The final project should reflect a premium product. All ideas encouraged. A label that is eye catching and gives of a pristine look. The wine is a Red Blend of Zinfandel, Syrah, Grenache, and Tempranillo. All Californian fruit and hand crafted. The wine is really something special and the label should reflect that. The label must also be able to carry many tiers, the addition of some other labels based around this label may take place in the future.

Target Market(s)

All ideas welcome

Industry/Entity Type

Retail

Font styles to use
Serif

Requirements
Must have
• Open to all ideas.
Nice to have
• An elegant look, simple colors, however, some sort of eye catching effect.
Should not have
• Should not be quirky.

```html
<!DOCTYPE html>
<html lang="en">
<head>
<meta charset="utf-8">
<title>Tamsel Zinfandel Labels</title>
<link rel="stylesheet" href="https://fonts.googleapis.com/css2?family=Cinzel:wght@400;700&display=swap">
<style>
  :root {
    --backdrop-light: #d9d9d9;
    --backdrop-dark: #a9a9a9;
    --label-black: #1c1c1c;
    --label-white: #f6f6f4;
    --gold: #c9a94e;
    --gold-deep: #8d7130;
    --ink: #111111;
    --crimson: #b0103a;
    --vintage-grey: #7a7a7a;
    --caption-light: #d8d8d8;
    --caption-dark: #2a2a2a;
  }
  * { margin: 0; padding: 0; box-sizing: border-box; }
  html, body {
    width: 1200px;
    height: 800px;
    overflow: hidden;
  }
  body {
    background: radial-gradient(ellipse at 50% 45%, var(--backdrop-light), var(--backdrop-dark));
    display: flex;
    align-items: center;
    justify-content: center;
    gap: 80px;
    font-family: "Cinzel", serif;
  }
  .label {
    width: 440px;
    height: 560px;
    display: flex;
    flex-direction: column;
    align-items: center;
    padding-top: 70px;
    box-shadow: 0 14px 40px rgba(0, 0, 0, 0.25);
  }
  .label--black { background: var(--label-black); }
  .label--white { background: var(--label-white); }

  .brand-name {
    font-weight: 700;
    font-size: 62px;
    letter-spacing: 1px;
    line-height: 1;
  }
  .label--black .brand-name { color: var(--gold); }
  .label--white .brand-name { color: var(--ink); }

  .brand-rule {
    width: 200px;
    height: 1px;
    background: var(--crimson);
    margin-top: 18px;
  }

  .ornament {
    margin-top: 34px;
    width: 170px;
    height: 170px;
  }

  .varietal {
    margin-top: 40px;
    color: var(--crimson);
    font-size: 38px;
    font-weight: 400;
    letter-spacing: 2px;
  }
  .vintage {
    margin-top: 10px;
    color: var(--vintage-grey);
    font-size: 18px;
    letter-spacing: 8px;
  }
  .region {
    margin-top: 34px;
    font-size: 18px;
    letter-spacing: 10px;
  }
  .label--black .region { color: var(--caption-light); }
  .label--white .region { color: var(--caption-dark); }
</style>
</head>
<body>
  <section class="label label--black">
    <h1 class="brand-name">TAMSEL</h1>
    <div class="brand-rule"></div>
    <svg class="ornament" viewBox="0 0 170 170" role="img" aria-label="Gold ornamental floral tile pattern in a diamond frame">
      <defs>
        <linearGradient id="gold-fill" x1="0" y1="0" x2="1" y2="1">
          <stop offset="0" stop-color="#c9a94e"/>
          <stop offset="1" stop-color="#8d7130"/>
        </linearGradient>
      </defs>
      <polygon points="85,4 166,85 85,166 4,85" fill="url(#gold-fill)"/>
    </svg>
    <p class="varietal">ZINFANDEL</p>
    <p class="vintage">2010</p>
    <p class="region">CALIFORNIA</p>
  </section>

  <section class="label label--white">
    <h1 class="brand-name">TAMSEL</h1>
    <div class="brand-rule"></div>
    <svg class="ornament" viewBox="0 0 170 170" role="img" aria-label="Black ornamental floral tile pattern in a diamond frame">
      <defs>
        <linearGradient id="ink-fill" x1="0" y1="0" x2="1" y2="1">
          <stop offset="0" stop-color="#2a2a2a"/>
          <stop offset="1" stop-color="#555555"/>
        </linearGradient>
      </defs>
      <polygon points="85,4 166,85 85,166 4,85" fill="url(#ink-fill)"/>
    </svg>
    <p class="varietal">ZINFANDEL</p>
    <p class="vintage">2010</p>
    <p class="region">CALIFORNIA</p>
  </section>
</body>
</html>
```